Business Card Design Project

We are an incubator company that helps young entrepreneur to launch new ideas into the market. We will be targeting investors or likewise; Angels, young entrepreneurs and technopreneurs.

Our logo is being tasked by artswarm to design, therefore there is no logo for now.
You can us Lanternfield Pte Ltd as the logo for the time being.

Please let us have some versions of modern and yet professional designs; for words, you can indicate e.g (address), (Title)

thanks

Target Market(s)

young entrepreneurs
angels, investors

Industry/Entity Type

Business

Colors
3176b5
ffffff

Requirements
Must have
• able to project out our name; Lanternfield
Should not have
• Nothing childish or cartoon

```html
<!DOCTYPE html>
<html lang="en">
<head>
<meta charset="utf-8">
<title>Lanternfield Business Card</title>
<link rel="stylesheet" href="https://fonts.googleapis.com/css2?family=Roboto:wght@400;500;700;900&display=swap">
<style>
  :root {
    --brand-blue: #3176b5;
    --brand-blue-deep: #1b5f9e;
    --brand-blue-light: #2f86c9;
    --paper: #ffffff;
    --paper-soft: #f3f3f4;
    --curve-shadow: #b9babd;
    --backdrop: #ececee;
    --ink-light: #ffffff;
  }
  * { box-sizing: border-box; margin: 0; padding: 0; }
  html, body {
    width: 1200px;
    height: 1001px;
    overflow: hidden;
    background: var(--backdrop);
    font-family: "Roboto", Arial, sans-serif;
  }
  .stage {
    position: relative;
    width: 1200px;
    height: 1001px;
  }
  .card {
    position: absolute;
    width: 500px;
    height: 286px;
    background: var(--paper);
    box-shadow: 0 8px 24px rgba(0,0,0,0.12);
    overflow: hidden;
  }
  .card--contact { left: 70px; top: 357px; }
  .card--brand { left: 630px; top: 357px; background: linear-gradient(135deg, var(--paper) 0%, var(--paper-soft) 100%); }

  .card__art { position: absolute; inset: 0; }

  .contact-list {
    position: absolute;
    left: 22px;
    top: 46px;
    list-style: none;
    color: var(--ink-light);
    font-size: 11.5px;
    line-height: 20px;
  }
  .contact-list li { display: flex; align-items: center; gap: 8px; white-space: nowrap; }
  .contact-list svg { width: 12px; height: 12px; flex: none; }

  .wordmark {
    position: absolute;
    display: flex;
    align-items: center;
    gap: 8px;
    color: var(--brand-blue);
    font-weight: 900;
    letter-spacing: 1px;
    text-transform: uppercase;
    white-space: nowrap;
  }
  .wordmark__square {
    width: 24px;
    height: 24px;
    background: var(--brand-blue);
    border-radius: 3px;
  }
  .card--contact .wordmark { left: 286px; top: 104px; font-size: 21px; }
  .card--brand .wordmark { left: 50%; top: 50%; transform: translate(-50%, -50%); font-size: 34px; gap: 10px; }
  .card--brand .wordmark__square { width: 36px; height: 36px; }

  .holder {
    position: absolute;
    right: 34px;
    bottom: 8px;
    color: var(--ink-light);
    text-align: right;
  }
  .holder__name { font-size: 15px; font-weight: 700; line-height: 18px; }
  .holder__title { font-size: 11px; font-weight: 400; line-height: 14px; }
</style>
</head>
<body>
<main class="stage">

  <section class="card card--contact">
    <svg class="card__art" viewBox="0 0 500 286" preserveAspectRatio="none" aria-hidden="true">
      <defs>
        <linearGradient id="bandGradient" x1="0" y1="0" x2="1" y2="1">
          <stop offset="0" stop-color="#1b5f9e"/>
          <stop offset="1" stop-color="#2f86c9"/>
        </linearGradient>
      </defs>
      <rect width="500" height="286" fill="url(#bandGradient)"/>
      <path d="M222,0 C242,155 335,230 500,244 L500,235 C340,222 250,150 230,0 Z" fill="#b9babd"/>
      <path d="M230,0 C250,150 340,222 500,235 L500,0 Z" fill="#f3f3f4"/>
    </svg>

    <ul class="contact-list">
      <li>
        <svg viewBox="0 0 12 12"><path d="M2 1h2l1 3-1.5 1a6 6 0 0 0 3.5 3.5L8 7l3 1v2a1 1 0 0 1-1 1A9 9 0 0 1 1 2a1 1 0 0 1 1-1z" fill="currentColor"/></svg>
        00.00.00.0000
      </li>
      <li>
        <svg viewBox="0 0 12 12"><rect x="2" y="1" width="8" height="4" fill="none" stroke="currentColor"/><rect x="1" y="5" width="10" height="6" fill="currentColor"/></svg>
        00.00.00.0000
      </li>
      <li>
        <svg viewBox="0 0 12 12"><rect x="1" y="2.5" width="10" height="7" fill="none" stroke="currentColor"/><path d="M1 2.5l5 4 5-4" fill="none" stroke="currentColor"/></svg>
        yourname@yourwebsite.com
      </li>
      <li>
        <svg viewBox="0 0 12 12"><circle cx="6" cy="6" r="5" fill="none" stroke="currentColor"/><path d="M1 6h10M6 1c-3 3-3 7 0 10M6 1c3 3 3 7 0 10" fill="none" stroke="currentColor"/></svg>
        www.yourwebsite.com
      </li>
      <li>
        <svg viewBox="0 0 12 12"><path d="M6 11S2 7 2 4.5a4 4 0 0 1 8 0C10 7 6 11 6 11z" fill="currentColor"/><circle cx="6" cy="4.5" r="1.4" fill="#3176b5"/></svg>
        Your Commercial or office address
      </li>
    </ul>

    <div class="wordmark">
      <span class="wordmark__square"></span>
      <span class="wordmark__name">Lanternfield</span>
    </div>

    <div class="holder">
      <p class="holder__name">Your Name</p>
      <p class="holder__title">Title</p>
    </div>
  </section>

  <section class="card card--brand">
    <div class="wordmark">
      <span class="wordmark__square"></span>
      <span class="wordmark__name">Lanternfield</span>
    </div>
  </section>

</main>
</body>
</html>
```